study by ripples circle

The website presents a new interactive learning system where it provides not only the teaching material as the instructor friend who can both teach and learn, making friends and making money.
Make friends and get money.

```html
<!DOCTYPE html>
<html lang="en">
<head>
<meta charset="utf-8">
<title>Study By Ripples Circle</title>
<link href="https://fonts.googleapis.com/css2?family=Lato:wght@300;400;700;900&family=Montserrat:wght@400;600&display=swap" rel="stylesheet">
<style>
:root{
  --brand:#1f9be6;
  --brand-light:#3fb4f2;
  --topbar:#0f4d96;
  --navy:#0c2f5a;
  --navy-deep:#08254a;
  --ink:#333a44;
  --muted:#6b7480;
  --soft:#9aa3ad;
  --white:#ffffff;
}
*{box-sizing:border-box;margin:0;padding:0}
html,body{width:674px;height:1200px;overflow:hidden}
body{position:relative;font-family:'Lato',sans-serif;font-weight:400;color:var(--ink);background:var(--white)}
.abs{position:absolute}

/* top bar */
.topbar{left:0;top:0;width:674px;height:21px;background:var(--topbar);color:var(--white);font-size:7px}
.topbar .contact{position:absolute;left:71px;top:4px;word-spacing:1px}
.topbar .contact span{margin-right:10px}
.social-top{position:absolute;right:70px;top:2px;display:flex;gap:4px}
.social-top i{display:block;width:16px;height:16px;border-radius:50%;background:var(--brand-light)}

/* header */
.header{left:0;top:21px;width:674px;height:50px;border-bottom:1px solid #e6e9ec}
.logo{position:absolute;left:74px;top:17px;display:flex;align-items:center;gap:5px;font-size:16px;color:var(--brand)}
.logo .dot{width:13px;height:13px;border-radius:50%;background:var(--brand)}
.nav{position:absolute;right:54px;top:23px;display:flex;gap:15px;font-size:9px;color:#4a4f57}

/* hero */
.hero{left:0;top:71px;width:674px;height:316px;background:radial-gradient(ellipse at 45% 45%,#e7b48f 0%,#b77654 35%,#6a4a3c 70%,#3e3a3c 100%)}
.hero-title{position:absolute;left:69px;top:176px;width:244px;height:74px;background:rgba(40,40,44,.72);padding:9px 10px;font-family:'Montserrat',sans-serif;font-weight:600;font-size:24px;line-height:32px;color:var(--white)}
.hero-title em{font-style:normal;color:var(--brand-light)}
.hero-badges{position:absolute;left:420px;top:100px}
.badge-text{font-family:'Montserrat',sans-serif;font-weight:600;fill:var(--brand)}

/* features */
.features{left:0;top:387px;width:674px;height:158px}
.feature{position:absolute;top:17px;width:120px;text-align:center}
.feature .icon{margin:0 auto;width:50px;height:50px;border-radius:50%;background:var(--brand);display:flex;align-items:center;justify-content:center}
.feature .icon.active{border:2px solid #2c3440}
.feature h3{margin-top:8px;font-weight:400;font-size:10.5px;letter-spacing:.3px;color:#222}
.feature .rule{width:78px;height:1px;background:#9fd4f3;margin:5px auto 6px}
.feature p{font-size:6.4px;font-weight:400;line-height:9.6px;color:#555}

/* who we are */
.who{left:0;top:545px;width:674px;height:202px;background:linear-gradient(100deg,#6b5a52 0%,#8a7668 40%,#a7968a 65%,#807066 100%)}
.who::after{content:"";position:absolute;inset:0;background:rgba(40,40,40,.28)}
.who h2{position:absolute;z-index:1;left:0;width:674px;top:9px;text-align:center;font-weight:400;font-size:17px;color:var(--white);letter-spacing:.3px}
.who-visual{position:absolute;z-index:1;left:74px;top:47px;width:195px;height:139px;background:radial-gradient(circle at 50% 45%,#1f6fb8 0%,#0f3f7e 60%,#0a2a58 100%);box-shadow:0 6px 10px rgba(0,0,0,.35)}
.who-list{position:absolute;z-index:1;top:46px;width:130px}
.who-list li{list-style:none;margin-bottom:9px}
.who-list b{display:block;font-weight:400;font-size:8.4px;color:var(--brand-light)}
.who-list b::before{content:"» ";color:var(--white)}
.who-list span{display:block;padding-left:9px;font-size:6.4px;font-weight:400;line-height:9.4px;color:var(--white)}

/* testimonials */
.testi{left:0;top:747px;width:674px;height:195px}
.testi h2{position:absolute;top:15px;width:674px;text-align:center;font-weight:400;font-size:17.5px;letter-spacing:2.6px;color:#2b3340}
.testi .sub{position:absolute;top:38px;width:674px;text-align:center;font-size:6.5px;line-height:11px;color:var(--soft)}
.quote{position:absolute;left:59px;top:91px;width:274px;height:48px;border:1px solid #e1e4e8;border-right:2px solid var(--brand);display:flex}
.quote .avatar{flex:0 0 48px;height:46px;background:linear-gradient(160deg,#d9c1ad,#8b6e5c)}
.quote p{padding:5px 8px;font-size:6.4px;font-weight:400;line-height:9.6px;color:#444}
.person{position:absolute;left:59px;top:148px}
.person b{display:block;font-size:8.4px;font-weight:700;color:#222}
.person small{display:block;font-size:6.5px;color:var(--soft);margin-top:3px}
.dots{position:absolute;left:60px;top:176px;display:flex;gap:3px}
.dots i{width:3px;height:3px;border-radius:50%;background:#c5cbd2}
.dots i.on{background:var(--brand)}
.client{position:absolute;width:96px;display:flex;align-items:center;justify-content:center;gap:5px;font-weight:700;font-size:11px}
.client i{display:block;width:11px;height:11px}

/* footer */
.footer{left:0;top:942px;width:674px;height:219px;background:var(--navy)}
.footer .logo{left:53px;top:40px;color:var(--brand-light);font-size:15px}
.footer p.about{position:absolute;left:56px;width:176px;font-size:6.4px;font-weight:400;line-height:11.5px;color:#6f86a3}
.read-more{position:absolute;left:56px;top:155px;display:flex;align-items:center;gap:4px;font-size:7px;font-weight:700;color:var(--white)}
.read-more i{width:7px;height:7px;border-radius:50%;background:var(--brand-light)}
.footer h4{position:absolute;top:42px;font-size:9.5px;letter-spacing:1px;font-weight:700;color:var(--white)}
.news{position:absolute;left:248px;width:178px;height:54px;border-bottom:1px solid #1b4270;display:flex;gap:10px}
.news .thumb{flex:0 0 38px;height:38px;background:linear-gradient(140deg,#c9d3dc,#6f7f90)}
.news b{display:block;font-size:8px;font-weight:400;color:#dfe8f2}
.news span{display:block;font-size:6.3px;line-height:9.6px;color:#6f86a3;margin-top:2px}
.news em{display:block;font-style:normal;font-size:6.3px;color:var(--brand-light);margin-top:2px}
.field{position:absolute;left:441px;width:177px;height:19px;background:#0a2850;border:1px solid #173c68;font-size:6.4px;color:#b7c5d6;padding:5px 7px;display:flex;justify-content:space-between}
.field.focus{border-color:#3d78b5}
.send{position:absolute;left:441px;top:167px;width:177px;height:19px;background:var(--brand-light);color:var(--white);font-size:7px;font-weight:700;letter-spacing:1px;text-align:center;line-height:19px}

/* bottom bar */
.bottom{left:0;top:1161px;width:674px;height:39px;background:var(--navy-deep);border-top:1px solid #123a66}
.bottom p{position:absolute;left:56px;top:15px;font-size:6.5px;color:#b7c5d6}
.bottom p em{font-style:normal;color:var(--brand-light)}
.social-foot{position:absolute;right:56px;top:16px;display:flex;gap:6px}
.social-foot i{display:block;width:6px;height:6px;border-radius:50%;background:#c8d3df}
</style>
</head>
<body>

<div class="abs topbar">
  <div class="contact"><span>24/7 Support: +1 555 014 2290</span>hello@ripplescircle.test</div>
  <div class="social-top"><i></i><i></i><i></i><i></i><i></i></div>
</div>

<header class="abs header">
  <div class="logo"><span class="dot"></span>Study By Ripples</div>
  <nav class="nav"><span>Home</span><span>About us</span><span>How it works</span><span>What we do</span><span>Contact Us</span></nav>
</header>

<section class="abs hero" role="img" aria-label="Photo of three smiling students gathered around a laptop">
  <div class="hero-title">Study by <em>Ripples</em><br><em>Circle</em></div>
  <svg class="hero-badges" width="200" height="200" viewBox="0 0 200 200" aria-hidden="true">
    <circle cx="72" cy="82" r="58" fill="#fff" stroke="#1f9be6" stroke-width="6"/>
    <circle cx="136" cy="68" r="31" fill="#fff" stroke="#1f9be6" stroke-width="5"/>
    <circle cx="145" cy="150" r="32" fill="#fff" stroke="#1f9be6" stroke-width="5"/>
    <text class="badge-text" x="72" y="79" font-size="18" text-anchor="middle">Make</text>
    <text class="badge-text" x="72" y="102" font-size="18" text-anchor="middle">Friends</text>
    <text class="badge-text" x="136" y="66" font-size="11" text-anchor="middle">Get</text>
    <text class="badge-text" x="136" y="80" font-size="11" text-anchor="middle">Money</text>
    <text class="badge-text" x="145" y="155" font-size="13" text-anchor="middle">Learn</text>
  </svg>
</section>

<section class="abs features">
  <div class="feature" style="left:72px">
    <div class="icon active"><svg width="16" height="16" viewBox="0 0 16 16"><path d="M15 1 1 7l5 2 2 6z" fill="#1f2733"/></svg></div>
    <h3>SUBSCRIBE</h3><div class="rule"></div>
    <p>Lorem ipsum dolor sit amet, consect-etuer adipiscing elit. Praesent vestibu-lum moles lacus. Aenean nonummy hendrerit.</p>
  </div>
  <div class="feature" style="left:209px">
    <div class="icon"><svg width="14" height="14" viewBox="0 0 14 14"><path d="M3 1h9l-2 12H1z" fill="#1f2733"/></svg></div>
    <h3>ONLINE COURSE</h3><div class="rule"></div>
    <p>Lorem ipsum dolor sit amet, consect-etuer adipiscing elit. Praesent vestibu-lum moles lacus. Aenean nonummy hendrerit.</p>
  </div>
  <div class="feature" style="left:346px">
    <div class="icon"><svg width="18" height="14" viewBox="0 0 18 14"><circle cx="5" cy="4" r="2.5" fill="#1f2733"/><circle cx="13" cy="4" r="2.5" fill="#1f2733"/><circle cx="9" cy="6" r="3" fill="#1f2733"/><rect x="1" y="8" width="16" height="5" rx="2.5" fill="#1f2733"/></svg></div>
    <h3>MAKE FRIENDS</h3><div class="rule"></div>
    <p>Lorem ipsum dolor sit amet, consect-etuer adipiscing elit. Praesent vestibu-lum moles lacus. Aenean nonummy hendrerit.</p>
  </div>
  <div class="feature" style="left:482px">
    <div class="icon"><svg width="18" height="12" viewBox="0 0 18 12"><rect x="1" y="1" width="16" height="10" fill="none" stroke="#1f2733" stroke-width="2"/><circle cx="9" cy="6" r="2.5" fill="#1f2733"/></svg></div>
    <h3>GET MONEY</h3><div class="rule"></div>
    <p>Lorem ipsum dolor sit amet, consect-etuer adipiscing elit. Praesent vestibu-lum moles lacus. Aenean nonummy hendrerit.</p>
  </div>
</section>

<section class="abs who" role="img" aria-label="Blurred photo of students studying together">
  <h2>WHO WE ARE</h2>
  <div class="who-visual" role="img" aria-label="Illustration of a chalk cloud raining study drops beside a light bulb"></div>
  <ul class="who-list" style="left:303px">
    <li><b>Who We are ?</b><span>Lorem ipsum dolor sit amet, consectetuer adipiscing elit.</span></li>
    <li><b>SBRC News</b><span>Lorem ipsum dolor sit amet, consectetuer adipiscing elit.</span></li>
    <li><b>Be a Friend Insructor</b><span>Lorem ipsum dolor sit amet, consectetuer adipiscing elit.</span></li>
    <li><b>Gives Your Suggestions</b><span>Lorem ipsum dolor sit amet, consectetuer adipiscing elit.</span></li>
  </ul>
  <ul class="who-list" style="left:442px">
    <li><b>Ripples</b><span>Lorem ipsum dolor sit amet, consectetuer adipiscing elit.</span></li>
    <li><b>Reports Your Findings</b><span>Lorem ipsum dolor sit amet, consectetuer adipiscing elit.</span></li>
    <li><b>Create Your Goute</b><span>Lorem ipsum dolor sit amet, consectetuer adipiscing elit.</span></li>
    <li><b>Advertise Your Products</b><span>Lorem ipsum dolor sit amet, consectetuer adipiscing elit.</span></li>
  </ul>
</section>

<section class="abs testi">
  <h2>TESTIMONIALS &amp; CLIENTS</h2>
  <div class="sub">Our design is coupled with the excellent value<br>Aliquam sit amet hendrerit non, placerat pulvinar enim</div>
  <div class="quote">
    <div class="avatar" role="img" aria-label="Portrait photo of the reviewer"></div>
    <p>Lorem ipsum dolor sit amet, consectetuer adipiscing elit. Lorem ipsum dolor sit amet, consectetuer adipiscing elit. Lorem ipsum dolor sit amet, consectetuer adipiscing elit. Lorem ipsum dolor sit amet, consectetuer adipiscing elit.</p>
  </div>
  <div class="person"><b>Tomas Verhelst</b><small>Web Developer</small></div>
  <div class="dots"><i></i><i></i><i class="on"></i><i></i></div>

  <div class="client" style="left:342px;top:104px;color:#2a7fc4"><i style="background:#2a7fc4;border-radius:50%"></i>Kestrel</div>
  <div class="client" style="left:438px;top:104px;color:#e2531f"><i style="background:#e2531f"></i>Nodo</div>
  <div class="client" style="left:534px;top:104px;color:#444"><i style="background:#f0792a;border-radius:50%"></i>Orbita</div>
  <div class="client" style="left:342px;top:158px;color:#1d4f8f"><i style="background:#e87c2a"></i>Facet</div>
  <div class="client" style="left:438px;top:158px;color:#555"><i style="background:#3a8ee0"></i>Quarrywise</div>
  <div class="client" style="left:534px;top:158px;color:#555"><i style="background:#62b846;border-radius:50%"></i>Huebox</div>
</section>

<footer class="abs footer">
  <div class="logo"><span class="dot" style="background:var(--brand-light)"></span>Study Ripples</div>
  <p class="about" style="top:78px">Nunc eu purus nec elit dapibus rutrum. Integer nibh dui, aliquet in leo eget, porta tincidunt quam.</p>
  <p class="about" style="top:112px">Vivamus non metus est. Etiam eu tellus justo. Vivamus plac-erat vestibulum eleifend. Sed viverra felis ante, id viverra enim pellentesque vitae.</p>
  <div class="read-more"><i></i>READ MORE</div>

  <h4 style="left:247px">LATEST NEWS</h4>
  <div class="news" style="top:69px">
    <div class="thumb" role="img" aria-label="Blog photo of a student at a laptop"></div>
    <div><b>Your Title Blog Here</b><span>Suspendisse consectetur ligula vitae leo faucibus, a tincidunt leo...</span><em>21 December, 2017</em></div>
  </div>
  <div class="news" style="top:131px">
    <div class="thumb" role="img" aria-label="Blog photo of students in class"></div>
    <div><b>Your Title Blog Here</b><span>Suspendisse consectetur ligula vitae leo faucibus, a tincidunt leo...</span><em>21 December, 2017</em></div>
  </div>

  <h4 style="left:440px">QUICK CONTACT US</h4>
  <div class="field" style="top:69px"><span>Name</span><span>&#9679;</span></div>
  <div class="field focus" style="top:93px"><span>you@mailbox.test</span><span>&#9634;</span></div>
  <div class="field" style="top:118px;height:43px"></div>
  <div class="send">SEND IT NOW</div>
</footer>

<div class="abs bottom">
  <p>Copyright 2014 <em>Ripples</em>. Designed by Northmark Studio</p>
  <div class="social-foot"><i></i><i></i><i></i><i></i><i></i><i></i><i></i><i></i></div>
</div>

</body>
</html>
```